Liquor Label / Aguardiente

Label design for liquor bottle. Designers may submit multiple submissions.

Product Description:
Name: Viento de Plata™
Alcohol Category: Aguardiente (which in Spanish most closely translates to “burning water”) – aguardiente is derived from
cane sugar and is a general term for a type of alcoholic spirit in many Central and South America countries.
Taste: A smooth liquor with a comfortable yet spicy finish
Smell: Subtle aroma of spicy jalapeños
Liquid Color: Clear
Bottle Color: Clear
See link for reference - http://www.kelvostamp.com/sites/default/files/styles/uc_product_full/public/Pemrow_0.jpg?itok=9QmT2xLp
Closure: Bar top / cork
Bottle Shape/Size: height = 8.67in; diameter of base = 3.70in; diameter of neck = 0.85in

Label may consist of two separate parts (i.e. front and back, front and vertical side), or one continuous label.

Designer has complete freedom with color, font etc. unless otherwise stated below. The label MUST
contain (but is not limited only to) the following text exactly as written in quotes below:
- “Viento de Plata”
- “Aguardiente”
- “Cane Neutral Spirit with Natural Flavors”
- “35% Alc./Vol.”
- “750 ml”
- “Bottled by WP Spirits, LLC” and “Nashville, TN” - “Government Warning: (1) According to the Surgeon General, women should not drink alcoholic beverages during
pregnancy because of the risk of birth defects. (2) Consumption of alcoholic beverages impairs your ability to
drive a car or operate machinery, and may cause health problems.” (text in previous quotes must be in all
capitalized letters, text must be 2 MM in height and quote must be separated 2MM by all other text)
- Must be dedicated empty space for bar code (approximately 0.75in. height x 1.25in. length)

Target Market(s)

Label should have mass market appeal.
Age: 21 – 28 years old (primary target market is 21+ year old college students and recent graduates)
Target Market Gender: Both male and female, with emphasis on male
Consumption Focus: Spirit will be consumed typically as a shot, primarily at bars and secondarily off premise (label design will be critical for making our product highly visible behind a bar)
Marketing Theme: South American elements. The official Viento de Plata mascot is a llama and the incorporation and use of a llama somewhere (however large or small) on the bottle is encourage but by no means required.

Industry/Entity Type

Health

Requirements
Should not have
• Elements that may lead a potential consumer to believe the beverage is a craft liquor or an artisan brand. Please do not include images of peppers.

```html
<!DOCTYPE html>
<html lang="en">
<head>
<meta charset="utf-8">
<title>Viento de Plata – Aguardiente Label</title>
<link href="https://fonts.googleapis.com/css2?family=Anton&family=Encode+Sans+Condensed:wght@400;700&display=swap" rel="stylesheet">
<style>
  :root {
    --ink: #000000;
    --brand-red: #d0141b;
    --sky-blue: #1e90e6;
    --mint: #43f59a;
    --white: #ffffff;
    --fire: #f08a1c;
    --ember: #b8300c;
    --water: #1646c8;
    --deep-water: #0a1a5a;
  }
  html, body {
    margin: 0;
    padding: 0;
    width: 1018px;
    height: 1200px;
    overflow: hidden;
    background: var(--ink);
  }
  .label {
    position: relative;
    width: 1018px;
    height: 1200px;
    background: var(--ink);
    overflow: hidden;
    font-family: "Encode Sans Condensed", "Arial Narrow", sans-serif;
  }
  .swirl-art {
    position: absolute;
    inset: 0 0 180px 0;
    background:
      radial-gradient(circle at 50% 52%, var(--ink) 0 150px, transparent 260px),
      radial-gradient(ellipse 420px 520px at 18% 40%, var(--fire) 0%, var(--ember) 35%, transparent 70%),
      radial-gradient(ellipse 520px 480px at 40% 6%, #f7b13a 0%, var(--ember) 30%, transparent 65%),
      radial-gradient(ellipse 520px 620px at 84% 58%, var(--water) 0%, var(--deep-water) 50%, transparent 80%),
      var(--ink);
  }
  .brand-name {
    position: absolute;
    top: 118px;
    left: 0;
    width: 1018px;
    margin: 0;
    text-align: center;
    font-family: "Anton", "Impact", sans-serif;
    font-weight: 400;
    font-size: 150px;
    line-height: 1;
    color: var(--brand-red);
  }
  .category {
    position: absolute;
    top: 518px;
    left: 412px;
    margin: 0;
    font-weight: 400;
    font-size: 74px;
    line-height: 1;
    color: var(--sky-blue);
    text-shadow: 0 0 3px var(--ink), 2px 2px 0 var(--ink), -2px -2px 0 var(--ink), 2px -2px 0 var(--ink), -2px 2px 0 var(--ink);
  }
  .description {
    position: absolute;
    top: 636px;
    left: 398px;
    margin: 0;
    font-weight: 700;
    font-size: 46px;
    line-height: 1.22;
    color: var(--mint);
    text-shadow: 2px 2px 0 var(--ink), -2px -2px 0 var(--ink), 2px -2px 0 var(--ink), -2px 2px 0 var(--ink);
  }
  .volume {
    position: absolute;
    top: 826px;
    left: 680px;
    margin: 0;
    font-weight: 400;
    font-size: 66px;
    line-height: 1;
    color: var(--white);
    text-shadow: 3px 3px 0 var(--ink), -3px -3px 0 var(--ink), 3px -3px 0 var(--ink), -3px 3px 0 var(--ink);
  }
  .base-wave {
    position: absolute;
    left: 0;
    bottom: 0;
    width: 1018px;
    height: 320px;
  }
  .abv {
    position: absolute;
    top: 1064px;
    left: 52px;
    margin: 0;
    font-weight: 700;
    font-size: 54px;
    line-height: 1;
    color: var(--mint);
  }
</style>
</head>
<body>
  <main class="label">
    <div class="swirl-art" role="img" aria-label="Swirling ring of flames on the left meeting a whirl of blue water with bubbles on the right"></div>

    <h1 class="brand-name">Viento de Plata</h1>

    <p class="category">AGUARDIENTE</p>
    <p class="description">CANE NEUTRAL SPIRIT<br>WITH NATURAL FLAVORS</p>
    <p class="volume">750 ml</p>

    <svg class="base-wave" viewBox="0 0 1018 320" aria-hidden="true">
      <path d="M0 60 C220 20 470 50 690 130 C840 185 950 205 1018 200 L1018 320 L0 320 Z" fill="var(--ink)"/>
      <path d="M0 60 C220 20 470 50 690 130 C840 185 950 205 1018 200 L1018 214 C940 222 830 204 680 150 C470 78 230 54 0 88 Z" fill="var(--brand-red)"/>
      <path d="M360 120 C560 150 760 240 1018 250 L1018 262 C760 256 560 170 360 124 Z" fill="var(--brand-red)"/>
    </svg>

    <p class="abv">35% Alc./Vol</p>
  </main>
</body>
</html>
```